Lumo Brew Premium Matcha brand Label

This is a label design project for a luxury tea brand. Feel free to be creative within the guidelines.
Attached to this project is a document called “Private Label Design Requirements” with the design guidelines and template. There is another document called "Lumo Brew Packaging Instructions" this has more details necessary to stick to the guidelines in the first document.

I have also attached the certifications to be included as well as different variations of the logo for you to use.

If you have any questions, I am here.
Updates

Target Market(s)

Young, active, fun, enjoy the finer things

```html
<!DOCTYPE html>
<html lang="en">
<head>
<meta charset="utf-8">
<title>Lumo Brew Premium Matcha Label</title>
<link rel="stylesheet" href="https://fonts.googleapis.com/css2?family=Roboto+Condensed:wght@400;700&display=swap">
<style>
  :root {
    --page: #ffffff;
    --board: #eeeff0;
    --leaf-green: #1f8b3b;
    --forest: #1c5a2c;
    --forest-deep: #17492a;
    --box-green: #1a7a34;
    --lime: #6cbf4a;
    --pale-lime: #bfe0a6;
    --ink-dark: #174a26;
    --white: #ffffff;
    --text-font: "Roboto Condensed", Arial, sans-serif;
  }
  * { margin: 0; padding: 0; box-sizing: border-box; }
  html, body { width: 1200px; height: 554px; overflow: hidden; background: var(--page); }
  body { position: relative; font-family: var(--text-font); color: var(--white); }

  .board { position: absolute; left: 20px; top: 40px; width: 1155px; height: 505px; background: var(--board); }

  .label { position: absolute; left: 47px; width: 1081px; height: 177px; display: flex; }
  .label--a { top: 88px; }
  .label--b { top: 307px; }

  .panel-side { position: relative; background: var(--leaf-green); height: 100%; }
  .panel-left { width: 269px; }
  .panel-right { width: 288px; }
  .panel-center { position: relative; width: 524px; height: 100%; }

  .leaf-pattern { position: absolute; inset: 0; background: radial-gradient(ellipse at center, var(--forest) 0%, var(--forest-deep) 100%); }

  .side-brand { position: absolute; left: 40px; top: 34px; display: flex; align-items: center; gap: 8px; font-weight: 700; font-size: 20px; }
  .brand-dot { width: 14px; height: 14px; border-radius: 50%; background: var(--white); }

  .origin { position: absolute; left: 48px; top: 104px; font-size: 13px; line-height: 16.5px; }
  .origin .lead { font-weight: 700; }

  .center-brand { position: absolute; left: 142px; top: 38px; width: 259px; text-align: center; font-weight: 700; font-size: 44px; letter-spacing: 1px; line-height: 48px; }

  .weight-box { position: absolute; left: 142px; width: 79px; background: var(--box-green); text-align: center; font-weight: 700; }
  .weight-box .tag { display: block; font-size: 12px; line-height: 14px; padding-top: 4px; }
  .weight-box .amount { display: block; font-size: 22px; line-height: 22px; }
  .weight-alt { position: absolute; left: 142px; width: 79px; text-align: center; font-size: 11px; }

  .grade-box { position: absolute; left: 221px; width: 180px; background: var(--lime); color: var(--ink-dark); font-weight: 700; font-size: 15px; line-height: 16px; letter-spacing: 0.5px; padding-left: 12px; display: flex; flex-direction: column; justify-content: center; }

  .label--a .weight-box, .label--a .grade-box { top: 92px; height: 44px; }
  .label--a .weight-alt { top: 138px; }

  .mark-square { position: absolute; left: 142px; top: 0; width: 79px; height: 92px; background: var(--pale-lime); color: var(--ink-dark); font-weight: 700; font-size: 12px; display: flex; flex-direction: column; align-items: center; justify-content: center; gap: 6px; }
  .mark-square .brand-dot { background: var(--ink-dark); width: 18px; height: 18px; }
  .center-name { position: absolute; left: 235px; top: 14px; font-weight: 700; font-size: 48px; line-height: 52px; letter-spacing: 1px; white-space: nowrap; }
  .label--b .weight-box, .label--b .grade-box { top: 92px; height: 42px; }
  .label--b .weight-alt { top: 136px; }

  .usage { position: absolute; left: 27px; top: 24px; font-size: 13px; line-height: 16.5px; }
  .usage .title { font-weight: 700; }
  .usage ul { list-style: none; padding-left: 7px; }
  .usage li::before { content: "· "; }

  .certs { position: absolute; left: 27px; top: 134px; display: flex; align-items: center; gap: 6px; }
  .cert-square { width: 30px; height: 28px; background: var(--white); }
  .cert-circle { width: 28px; height: 28px; border-radius: 50%; background: var(--white); }
  .storage { margin-left: 8px; font-weight: 700; font-size: 12.5px; line-height: 15px; }
</style>
</head>
<body>
  <div class="board"></div>

  <section class="label label--a">
    <div class="panel-side panel-left">
      <div class="side-brand"><span class="brand-dot"></span>Lumo Brew</div>
      <p class="origin"><span class="lead">Product of Japan</span><br>Distributed by Lumo Brew Co. | Brookvale, Ga<br>Certified Organic by certora</p>
    </div>
    <div class="panel-center">
      <div class="leaf-pattern" role="img" aria-label="Faint tea leaf pattern on deep green"></div>
      <div class="center-brand">LUMO BREW</div>
      <div class="weight-box"><span class="tag">Net Wt:</span><span class="amount">30g</span></div>
      <div class="grade-box"><span>PREMIUM ORGANIC</span><span>CEREMONIAL MATCHA</span></div>
      <div class="weight-alt">1.06oz</div>
    </div>
    <div class="panel-side panel-right">
      <div class="usage">
        <p class="title">Premium Organic Japanese Matcha Green Tea</p>
        <p>Instructions:</p>
        <ul>
          <li>2 tsp of Matcha</li>
          <li>2oz of Water (170-180 degrees F)</li>
          <li>Whisk in a W formation until frothy</li>
          <li>Sweeten to taste</li>
        </ul>
      </div>
      <div class="certs">
        <span class="cert-square"></span><span class="cert-circle"></span>
        <span class="storage">KEEP REFRIGERATED<br>FOR QUALITY</span>
      </div>
    </div>
  </section>

  <section class="label label--b">
    <div class="panel-side panel-left">
      <div class="side-brand"><span class="brand-dot"></span>Lumo Brew</div>
      <p class="origin"><span class="lead">Product of Japan</span><br>Distributed by Lumo Brew Co. | Brookvale, Ga<br>Certified Organic by certora</p>
    </div>
    <div class="panel-center">
      <div class="leaf-pattern" role="img" aria-label="Faint tea leaf pattern on deep green"></div>
      <div class="mark-square"><span class="brand-dot"></span>Lumo Brew</div>
      <div class="center-name">LUMO BREW</div>
      <div class="weight-box"><span class="tag">Net Wt:</span><span class="amount">30g</span></div>
      <div class="grade-box"><span>PREMIUM ORGANIC</span><span>CEREMONIAL MATCHA</span></div>
      <div class="weight-alt">1.06oz</div>
    </div>
    <div class="panel-side panel-right">
      <div class="usage">
        <p class="title">Premium Organic Japanese Matcha Green Tea</p>
        <p>Instructions:</p>
        <ul>
          <li>2 tsp of Matcha</li>
          <li>2oz of Water (170-180 degrees F)</li>
          <li>Whisk in a W formation until frothy</li>
          <li>Sweeten to taste</li>
        </ul>
      </div>
      <div class="certs">
        <span class="cert-square"></span><span class="cert-circle"></span>
        <span class="storage">KEEP REFRIGERATED<br>FOR QUALITY</span>
      </div>
    </div>
  </section>
</body>
</html>
```